I am looking for a poster design with a pledge for my clients to take. The pledge will be to not use tanning beds. Our company is a Spray Tanning Salon that focuses on educating our clients on the dangers of indoor tanning while offering a safe alternative through spray tanning. I have an outline of a possible wording but I am VERY open to adjustments on it!
This is not a promotional poster. This is a poster that will be hanging in the salon and our clients will sign around the wall.
Updates

Project Deadline Extended Reason: Not currently in love with any submissions and would like to see more. Looking for a more simple design overall. Added Friday, October 28, 2016

Target Market(s)

Women 20-30 years old

Industry/Entity Type

Salon

Font styles to use
Sans Serif

Requirements
Must have
• Take the pledge to ditch the bed!
• Willowmere Tanning
• **Overall simple design, yet eye catching is requested. Not so busy**
Nice to have
• I am open to different wording!
• I pledge to be timeless
• -UVA rays in tanning beds cause wrinkles and other signs of premature aging
• I pledge to be fearless
• -Using tanning beds can cause severe eye damage, a weakened immune system, and melanoma the deadliest form of skin cancer.
• I pledge to be Sunless!
• -Join the LumaVeil revolution at Willowmere Tanning, Grand Rapids first Sunless Spa Experience.
Should not have
• The photo of the salon on it. I included that photo simply for reference of design, this is where this poster will be hung.

```html
<!DOCTYPE html>
<html lang="en">
<head>
<meta charset="utf-8">
<title>Willowmere Tanning – Take the Pledge</title>
<link rel="stylesheet" href="https://fonts.googleapis.com/css2?family=Arimo:wght@400&display=swap">
<style>
  :root {
    --page: #ffffff;
    --paper: #dcdcdc;
    --ink: #000000;
    --reverse: #ffffff;
    --accent: #3ccf9a;
  }
  * { margin: 0; padding: 0; box-sizing: border-box; }
  html, body {
    width: 900px;
    height: 1200px;
    overflow: hidden;
    background: var(--page);
    font-family: "Arimo", Arial, sans-serif;
  }
  .poster {
    position: relative;
    width: 900px;
    height: 1200px;
  }
  .poster-frame {
    position: absolute;
    left: 0; top: 0;
  }
  .brand {
    position: absolute;
    left: 108px;
    top: 112px;
    display: flex;
    align-items: center;
    gap: 10px;
    color: var(--ink);
    font-size: 25px;
    letter-spacing: 0.5px;
  }
  .brand-mark {
    width: 16px;
    height: 16px;
    background: var(--accent);
  }
  .sprayer-area {
    position: absolute;
    left: 120px;
    top: 306px;
    width: 533px;
    height: 731px;
    background: var(--ink);
    border-radius: 28px;
  }
  .copy {
    position: absolute;
    color: var(--reverse);
    transform: translate(-50%, -50%) rotate(var(--angle));
    white-space: nowrap;
  }
  .pledge {
    font-size: 26px;
    line-height: 1.12;
  }
  .pledge-sunless { left: 218px; top: 504px; --angle: -20deg; }
  .pledge-timeless { left: 378px; top: 383px; --angle: -20deg; }
  .pledge-fearless { left: 278px; top: 632px; --angle: 90deg; }
  .fact {
    font-size: 20px;
    line-height: 1.15;
    text-align: center;
  }
  .fact-aging { left: 530px; top: 552px; --angle: 62deg; }
  .fact-health { left: 428px; top: 852px; --angle: 64deg; }
  .fact-aging-small {
    left: 268px; top: 780px; --angle: -6deg;
    font-size: 14px;
    line-height: 1.6;
    text-align: left;
  }
  .invite {
    left: 325px; top: 930px; --angle: -5deg;
    font-size: 19px;
    line-height: 1.18;
    text-align: left;
  }
</style>
</head>
<body>
<main class="poster">
  <svg class="poster-frame" width="900" height="1200" viewBox="0 0 900 1200" aria-hidden="true">
    <defs>
      <clipPath id="frame-clip">
        <rect x="55" y="42" width="790" height="1124" rx="8"/>
      </clipPath>
    </defs>
    <rect x="55" y="42" width="790" height="1124" rx="8" fill="var(--paper)"/>
    <path class="side-wave" clip-path="url(#frame-clip)" fill="var(--ink)"
          d="M647 42 C720 150 770 300 755 430 C742 540 700 620 712 740 C724 860 770 980 762 1166 L845 1166 L845 42 Z"/>
    <rect x="55" y="42" width="790" height="1124" rx="8" fill="none" stroke="var(--ink)" stroke-width="3"/>
  </svg>

  <header class="brand">
    <span class="brand-mark"></span>
    <span class="brand-name">Willowmere Tanning</span>
  </header>

  <div class="sprayer-area" role="img" aria-label="Black silhouette of a spray tan gun with cup, holding the pledge text"></div>

  <p class="copy pledge pledge-sunless">I pledge<br>to be Sunless</p>
  <p class="copy pledge pledge-timeless">I pledge<br>be timeless</p>
  <p class="copy pledge pledge-fearless">I pledge to<br>be fearless</p>

  <p class="copy fact fact-aging">UVA rays in tanning beds cause<br>wrinkles and other signs<br>of premature aging</p>

  <p class="copy fact fact-aging-small">UVA rays in tanning<br>beds cause wrinkles<br>and other signs of<br>premature aging</p>

  <p class="copy invite">Join the<br>LumaVeil<br>revolution<br>Willowmere<br>Tanning,<br>Grand Rapids<br>first Sunless<br>Spa Experience</p>

  <p class="copy fact fact-health">Using tanning beds can cause<br>severe eye damage, a weakened<br>immune system, and melanoma the<br>deadliest form of skin cancer.</p>
</main>
</body>
</html>
```